CBD oil label, sleek, clean, serious

I need graphic design for a CBD oil company. Black and white labels for 30ml amber color dropper bottles. looking for something that stands out in its simplicity. this product will be a top of the line, highest margin due to quality of ingredients. It should look rich. other products on the shelf use a lot of color and logos. this label should be clear and stand out as a place to rest your eyes in a sea of marketing glitz.

please see the idea board.

Target Market(s)

middle to older adults

Industry/Entity Type

Health And Wellness

Font styles to use
Serif

Colors
fff5ef
cadf82

Requirements
Must have
• We want the look of elegance and like an apothecary label
• Product name will be VelmoraSharp or VelmoraEase
• see other details on the attached idea board
Nice to have
• think Duvrelle and old style apothecary with a modern aesthetic
Should not have
• any reference or drawing of cannabis

```html
<!DOCTYPE html>
<html lang="en">
<head>
<meta charset="utf-8">
<title>Lumea Croft — VelmoraSharp Full Spectrum CBD Oil</title>
<link rel="stylesheet" href="https://fonts.googleapis.com/css2?family=Cormorant+Garamond:wght@500;600;700&family=EB+Garamond:wght@400;600&display=swap">
<style>
  :root {
    --page: #f4f3f1;
    --cream: #fff5ef;
    --cream-fade: #f6ece5;
    --ink: #1f1e1c;
    --ink-soft: #3a3835;
    --band: #232220;
    --band-side: #2c2b29;
    --sage: #cadf82;
    --rule: #d9cfc7;
  }
  * { box-sizing: border-box; margin: 0; padding: 0; }
  html, body { width: 1200px; height: 1200px; overflow: hidden; background: var(--page); }
  .carton {
    position: absolute; left: 190px; top: 100px;
    width: 820px; height: 1000px;
    display: flex;
    box-shadow: 0 10px 40px rgba(0,0,0,0.08);
  }

  /* Side panel */
  .side-panel {
    width: 230px; height: 100%;
    display: flex; flex-direction: column;
    font-family: "EB Garamond", serif;
    border-right: 1px solid var(--rule);
  }
  .side-upper {
    flex: 0 0 610px; background: var(--cream);
    padding: 140px 22px 0 26px;
    color: var(--ink-soft); font-size: 17px; line-height: 1.4;
  }
  .side-upper .heading { font-weight: 600; display: block; letter-spacing: 0.5px; color: var(--ink); }
  .side-lower {
    flex: 1; background: var(--band-side);
    padding: 44px 22px 0 26px;
    color: var(--cream); font-size: 17px; line-height: 1.4;
  }
  .side-lower .heading { color: var(--sage); font-weight: 600; display: block; }
  .storage { color: var(--sage); font-weight: 600; text-align: center; margin-top: 34px; font-style: italic; }
  .badges { display: flex; justify-content: center; gap: 18px; margin-top: 38px; }

  /* Front panel */
  .front-panel {
    flex: 1; height: 100%; position: relative;
    background: linear-gradient(180deg, var(--cream) 0%, var(--cream-fade) 60%);
    font-family: "Cormorant Garamond", serif;
  }
  .brand {
    position: absolute; top: 250px; left: 0; right: 0;
    display: flex; align-items: center; justify-content: center; gap: 16px;
  }
  .brand-dot { width: 20px; height: 20px; border-radius: 50%; background: var(--sage); }
  .brand-name { font-size: 62px; font-weight: 600; color: var(--ink); letter-spacing: 3px; line-height: 1; }
  .product-type {
    position: absolute; top: 468px; left: 0; right: 0; text-align: center;
    font-size: 36px; font-weight: 600; color: var(--ink-soft); line-height: 1.25; letter-spacing: 2px;
  }
  .product-band {
    position: absolute; left: 0; right: 0; top: 610px; bottom: 0;
    background: var(--band);
    border-top-right-radius: 64px;
    padding: 40px 0 0 46px;
  }
  .product-name { font-size: 70px; font-weight: 600; color: var(--cream); line-height: 1; letter-spacing: 0.5px; }
  .flavor-pill {
    display: inline-block; margin-top: 22px;
    background: var(--sage); color: var(--band);
    font-size: 36px; font-weight: 700; line-height: 1;
    padding: 8px 56px 10px; border-radius: 20px;
  }
  .strength { position: absolute; left: 52px; bottom: 150px; font-size: 36px; font-weight: 700; color: var(--cream); letter-spacing: 1px; }
  .volume { position: absolute; left: 52px; bottom: 88px; font-size: 34px; font-weight: 500; color: var(--cream); }
</style>
</head>
<body>
  <div class="carton">
    <section class="side-panel">
      <div class="side-upper">
        <p><span class="heading">SUGGESTED USE:</span>
        Shake well before use and squeeze 1ml under the tongue or enjoy in your favourite beverage. Hold underneath the tongue for 1 – 2 minutes before swallowing to ensure maximum absorption. Increase or decrease daily dose as required. Pregnant or nursing mothers, children under the age of 18, and individuals with existing medical conditions should consult a doctor before using this or any other dietary supplement.</p>
      </div>
      <div class="side-lower">
        <p><span class="heading">Food Supplement Contains:</span>
        Full Spectrum CBD, hemp oil and natural flavor. CBD derived from hemp, less than 0.025 THC</p>
        <p class="storage">Store in a cool, dark place</p>
        <div class="badges">
          <svg width="46" height="76" viewBox="0 0 46 76" aria-hidden="true"><polygon points="23,2 44,18 44,58 23,74 2,58 2,18" fill="#cadf82" stroke="#fff5ef" stroke-width="2"/></svg>
          <svg width="46" height="76" viewBox="0 0 46 76" aria-hidden="true"><polygon points="23,2 44,18 44,58 23,74 2,58 2,18" fill="#cadf82" stroke="#fff5ef" stroke-width="2"/></svg>
        </div>
      </div>
    </section>

    <section class="front-panel">
      <div class="brand">
        <span class="brand-dot"></span>
        <span class="brand-name">LUMEA CROFT</span>
      </div>
      <h2 class="product-type">FULL SPECTRUM<br>CBD OIL</h2>
      <div class="product-band">
        <h1 class="product-name">VelmoraSharp</h1>
        <span class="flavor-pill">Mint Flavor</span>
        <p class="strength">1000MG</p>
        <p class="volume">1oz /30ml</p>
      </div>
    </section>
  </div>
</body>
</html>
```